Business Card and Letterhead for Vantel Psychology

We need a business card design and letterhead to use for our Psychology firm that specializes in psychoeducational assessments and individual therapy. Our motto is Purpose-Driven Assessments, Meaning-Centered Therapy.Our contact information is as follows:
Vantel Psychology
The Bramwick Block - 4127-38St.
Box 6154 Ashvale, QX
T2K 3R8
t 403.555.0148 (VANT)
f 403.555.0193
www.vantelpsych-example.ca
The business card will be used for two different psychologists so I can supply names nearer to completion. We prefer clean, uncluttered looks.

Target Market(s)

Clients, Educators

Font styles to use
Sans Serif

Colors

Designer to choose colors to be used in the design.

Requirements
Must have
• All relevant contact info, logo, some "white" space.
Nice to have
• It would be nice to see letterhead options that have the logo on the top of the page but also options that have it on the side. I think top of the page is probably our preference.
Should not have
• Too much clutter!

```html
<!DOCTYPE html>
<html lang="en">
<head>
<meta charset="utf-8">
<title>Vantel Psychology – Business Card</title>
<link href="https://fonts.googleapis.com/css2?family=Source+Sans+3:wght@400;600;700&display=swap" rel="stylesheet">
<style>
  :root{
    --stage:#3a3b3e;
    --card:#1a1b1d;
    --edge:#3bb4d8;
    --cyan:#3bb4d8;
    --orange:#f5a04a;
    --ink:#e9e9ea;
    --rule:#5a5b5e;
    --mark:#2b2c2f;
  }
  *{box-sizing:border-box;margin:0;padding:0}
  html,body{width:1200px;height:779px;overflow:hidden}
  body{background:var(--stage);font-family:"Source Sans 3",sans-serif;color:var(--ink);position:relative}
  .card{position:absolute;top:230px;width:560px;height:320px;background:var(--card);border-bottom:4px solid var(--edge);border-left:2px solid var(--edge);box-shadow:0 14px 30px rgba(0,0,0,.45)}
  .card--back{left:20px}
  .card--front{left:620px}

  /* back */
  .back-brand{position:absolute;left:0;right:0;top:90px;display:flex;flex-direction:column;align-items:center;gap:14px}
  .back-brand__dot{width:90px;height:90px;border-radius:50%;background:var(--mark)}
  .back-brand__name{font-size:18px;font-weight:600;letter-spacing:3px;color:#8a8b8e;text-transform:uppercase}
  .tagline{position:absolute;left:0;right:0;bottom:44px;text-align:center;font-size:15px;letter-spacing:.3px}

  /* front */
  .brand{position:absolute;left:20px;top:104px;width:266px;display:flex;flex-direction:column;align-items:center;gap:14px}
  .brand__dot{width:72px;height:72px;border-radius:50%;background:var(--cyan)}
  .brand__name{font-size:21px;font-weight:600;letter-spacing:2px;color:var(--cyan);text-transform:uppercase;white-space:nowrap}
  .divider{position:absolute;left:294px;top:70px;width:1px;height:180px;background:var(--rule)}
  .contact{position:absolute;left:310px;top:64px;width:240px}
  .contact__name{font-size:17px;font-weight:700;color:var(--cyan);line-height:1.15}
  .contact__creds{font-size:11px;font-weight:600;color:var(--cyan);line-height:1.3}
  .contact__role{font-size:12.5px;color:var(--orange);margin-bottom:10px}
  .contact__addr{font-size:12.5px;line-height:1.4;margin-bottom:8px}
  .contact__list{list-style:none;font-size:12.5px;line-height:1.6}
  .contact__list li{display:flex;align-items:center;gap:7px;white-space:nowrap}
  .icon{width:11px;height:11px;flex:none;fill:var(--orange)}
</style>
</head>
<body>

<section class="card card--back" aria-label="Business card back">
  <div class="back-brand">
    <span class="back-brand__dot"></span>
    <span class="back-brand__name">Vantel Psychology</span>
  </div>
  <p class="tagline">Thoughtful Evaluations | Growth-Focused Counselling.</p>
</section>

<section class="card card--front" aria-label="Business card front">
  <div class="brand">
    <span class="brand__dot"></span>
    <span class="brand__name">Vantel Psychology</span>
  </div>
  <div class="divider"></div>
  <div class="contact">
    <p class="contact__name">Maren Oakley-Dunmore</p>
    <p class="contact__creds">M.Ed., R.Psych</p>
    <p class="contact__role">Registered Psychologist</p>
    <p class="contact__addr">The Bramwick Block - 4127-38St.<br>Box 6154 Ashvale, QX T2K 3R8</p>
    <ul class="contact__list">
      <li><svg class="icon" viewBox="0 0 12 12"><path d="M1 4c0-2 2-3 5-3s5 1 5 3H8V3H4v1z"/><rect x="2" y="5" width="8" height="6" rx="1"/></svg>403.555.0148 (VANT)</li>
      <li><svg class="icon" viewBox="0 0 12 12"><rect x="3" y="1" width="6" height="4"/><rect x="1" y="5" width="10" height="6" rx="1"/></svg>403.555.0193</li>
      <li><svg class="icon" viewBox="0 0 12 12"><path d="M1 3h10v7H1z"/><path d="M1 3l5 4 5-4" fill="none" stroke="#1a1b1d" stroke-width="1"/></svg>maren@vantelpsych-example.ca</li>
      <li><svg class="icon" viewBox="0 0 12 12"><circle cx="6" cy="6" r="5.5"/><path d="M3 4h4v3H5v2" fill="none" stroke="#1a1b1d" stroke-width="1"/></svg>www.vantelpsych-example.ca</li>
    </ul>
  </div>
</section>

</body>
</html>
```